US Based Startup requires Website Design for Kavrelon Cell

We are launching a battery technology called "Kavrelon Cell" for which we need an elegant website design. We use red and black to represent positive and negative node color used in battery. The background is white. The font must provide more wide space and easy to read.
Kavrelon CellTM is a technology that uses fast switches, such as transistor switches, to make batteries more efficient. The novel technology can be implemented in all types of batteries – including non-rechargeable batteries, rechargeable batteries, wet-cell batteries and all metal oxide batteries.
Normal batteries are “non-switching”, that is, these batteries can only be connected to one another in parallel or series connections. Parallel connections enable batteries to charge faster whilst series connections enable the battery to discharge more efficiently to the load.
Kavrelon CellTM technology enables batteries to be connected in a third connection method called “vexa-loopTM” that combines the benefit of faster charging of the batteries with renewable energy source, such as solar, in parallel connection, and then quickly re-configures the same batteries using the fast transistor switches, to be connected in series with the load, to discharge efficiently.

Target Market(s)

Renewable energy

Industry/Entity Type

Renewable

Coding

Coded - Design and coding required

Number of Pages Required

5+ page

Requirements
Must have
• The primary colors are red and black for logo and fonts. The background is white.
The font must be easy to read type of fonts with more white space. Only pictures will be in full color.
Nice to have
• Elegant and simple design bringing out a new battery concept to the energy industry.

```html
<!DOCTYPE html>
<html lang="en">
<head>
<meta charset="utf-8">
<title>Kavrelon Cell — Trusted Batteries</title>
<link href="https://fonts.googleapis.com/css2?family=Oswald:wght@400;500;600&family=Lato:wght@400;700;900&display=swap" rel="stylesheet">
<style>
:root{
  --red:#ee3232;
  --red-deep:#d92323;
  --black:#141414;
  --ink:#1d1d1d;
  --dark:#1a1a1a;
  --grey-card:#f3f2f0;
  --white:#ffffff;
  --muted:#555555;
  --gold:#f6c21c;
}
*{margin:0;padding:0;box-sizing:border-box}
html,body{width:1200px;height:3750px;overflow:hidden;background:var(--white)}
body{position:relative;font-family:"Lato",Arial,sans-serif;color:var(--ink)}
.abs{position:absolute}
.heading{font-family:"Oswald",Arial Narrow,sans-serif;font-weight:500;text-transform:uppercase;letter-spacing:-0.5px;line-height:1}
.btn{position:absolute;display:flex;align-items:center;justify-content:center;font-family:"Oswald",sans-serif;font-weight:500;text-transform:uppercase;font-size:18px;border-radius:4px}

/* hero */
.hero{position:absolute;left:0;top:0;width:1200px;height:553px;background:radial-gradient(ellipse at 55% 40%,#3a3a3a 0%,#1c1c1c 55%,#0c0c0c 100%)}
.logo{left:58px;top:24px;color:var(--white);font-family:"Lato",sans-serif;font-weight:900;font-size:29px;letter-spacing:-0.3px}
.tagline{left:59px;top:57px;color:var(--white);font-size:10.5px;font-weight:700;letter-spacing:2px}
.nav{left:600px;top:28px;display:flex;align-items:center}
.nav a{color:var(--white);text-decoration:none;font-size:13px;font-weight:700;padding:6px 14px;text-transform:uppercase}
.nav a.active{background:var(--red);border-radius:14px}
.call-label{left:0;width:1200px;top:104px;text-align:center;color:var(--red);font-size:36px}
.call-phone{left:0;width:1200px;top:142px;text-align:center;color:var(--white);font-family:"Lato",sans-serif;font-weight:700;font-size:57px;letter-spacing:-1px}
.call-url{left:0;width:1200px;top:204px;text-align:center;color:var(--white);font-size:24px}
.hero-products{left:270px;top:240px;width:662px;height:418px;border-radius:6px;background:linear-gradient(160deg,#ff4a4a 0%,#e01f1f 55%,#8e1010 100%);z-index:3}

/* intro band */
.intro{position:absolute;left:0;top:553px;width:1200px;height:532px;background:var(--red)}
.eyebrow-white{left:160px;top:671px;color:var(--white);font-size:26px}
.intro-title{left:160px;top:714px;color:var(--white);font-size:38px;line-height:1.08}
.intro-text{left:163px;top:802px;width:540px;color:var(--white);font-size:17.5px;line-height:1.25}
.btn-white{left:161px;top:948px;width:124px;height:36px;background:var(--white);color:var(--red)}
.booking{left:740px;top:671px;width:316px;height:353px;background:var(--white);box-shadow:0 6px 18px rgba(0,0,0,.25)}
.booking-head{height:57px;background:var(--black);padding:16px 26px;color:var(--white);font-size:26px}
.booking-head span{color:var(--red)}
.field{position:absolute;border-bottom:1px solid #cfcfcf;font-family:"Oswald",sans-serif;font-size:12px;color:#333;text-transform:uppercase;padding-bottom:6px}
.btn-submit{left:15px;top:304px;width:282px;height:33px;background:var(--black);color:var(--red);font-size:20px;border-radius:5px}

/* products */
.section-eyebrow{left:0;width:1200px;text-align:center;color:var(--red);font-size:27px}
.section-title{left:0;width:1200px;text-align:center;color:var(--black);font-size:40px}
.card{position:absolute;top:1281px;width:280px;height:316px;background:var(--grey-card);text-align:center}
.card.featured{background:var(--red)}
.card-photo{position:absolute;top:-73px;left:74px;width:132px;height:129px;border-radius:4px;background:linear-gradient(150deg,#ff4b4b,#c41818 70%,#6b1f10)}
.card h3{position:absolute;top:83px;width:100%;font-size:29px;color:var(--black)}
.card p{position:absolute;top:128px;left:20px;width:240px;font-size:15px;line-height:1.25;color:var(--muted)}
.card .price{position:absolute;top:202px;width:100%;font-size:46px;color:var(--red);font-weight:600}
.card.featured h3,.card.featured p,.card.featured .price{color:var(--white)}
.card .btn{top:262px;left:78px;width:125px;height:35px;background:var(--red);color:var(--white)}
.card.featured .btn{background:var(--black)}
.corner{position:absolute;right:0;bottom:0}

/* services */
.services{position:absolute;left:0;top:1655px;width:1200px;height:565px;background:radial-gradient(ellipse at 50% 60%,#2e2f33 0%,#17181b 60%,#0b0b0c 100%)}
.feature-icon{position:absolute;width:60px;height:60px;border-radius:50%;background:var(--red);display:flex;align-items:center;justify-content:center}
.feature-title{position:absolute;color:var(--red);font-size:25px}
.feature-text{position:absolute;width:310px;color:var(--white);font-size:18px;line-height:1.25}
.btn-red{background:var(--red);color:var(--white)}

/* about */
.about-eyebrow{left:175px;top:2303px;color:var(--red);font-size:27px}
.about-title{left:175px;top:2335px;color:var(--black);font-size:40px}
.about-text{left:175px;top:2385px;width:580px;font-size:17.5px;line-height:1.27;color:var(--muted)}
.btn-dark{left:175px;top:2514px;width:123px;height:37px;background:var(--black);color:var(--red)}
.about-icon{position:absolute;top:2583px;width:47px;height:47px;border-radius:50%;border:2px solid var(--black);display:flex;align-items:center;justify-content:center}
.about-icon.hot{border-color:var(--red)}
.about-products{left:770px;top:2330px;width:395px;height:320px;border-radius:6px;background:linear-gradient(135deg,#ff5050 0%,#e02222 50%,#a51515 100%)}

/* testimonials */
.testimonials{position:absolute;left:0;top:2708px;width:1200px;height:459px;background:linear-gradient(180deg,#2b2b2b,#1e1e1e)}
.quote{position:absolute;top:2929px;width:434px;height:172px;background:#111;border-radius:28px;padding:28px 38px;color:var(--white)}
.quote p{font-size:15px;line-height:1.45}
.avatar{position:absolute;left:36px;top:104px;width:52px;height:52px;border-radius:50%;background:linear-gradient(160deg,#8a7a6e,#3d3430)}
.quote .name{position:absolute;left:102px;top:106px;color:var(--red);font-size:20px}
.quote .role{position:absolute;left:102px;top:130px;font-size:15px;text-transform:uppercase}

/* cta */
.cta{position:absolute;left:0;top:3167px;width:1200px;height:214px;background:var(--red)}
.cta-text{left:0;width:1200px;top:3220px;text-align:center;color:var(--white);font-size:33px}
.cta-phone{left:0;width:1200px;top:3267px;text-align:center;color:var(--white);font-size:58px;font-weight:400}

/* footer */
.footer{position:absolute;left:0;top:3381px;width:1200px;height:369px;background:linear-gradient(180deg,#1e1e1e,#141414)}
.foot-head{position:absolute;color:var(--red);font-size:19px}
.foot-rule{position:absolute;top:3490px;width:255px;height:5px;background:var(--red)}
.foot-text{position:absolute;color:var(--white);font-size:15px;line-height:1.3}
.foot-list{position:absolute;list-style:none;color:var(--white);font-size:15px}
.foot-list li{margin-bottom:19px}
.foot-list li::before{content:"";display:inline-block;width:5px;height:5px;background:var(--red);margin-right:8px;vertical-align:middle}
.contact-row{position:absolute;left:804px;display:flex;gap:24px;color:var(--white);font-size:15px;line-height:1.15}
.contact-row svg{flex:none;margin-top:2px}
.social{position:absolute;top:3631px;left:160px;display:flex;gap:14px}
.social span{width:11px;height:11px;border-radius:50%;background:var(--white)}
.social span.hot{background:var(--red)}
.copyright{left:0;width:1200px;top:3726px;text-align:center;color:var(--white);font-size:10px}
</style>
</head>
<body>

<!-- hero -->
<section class="hero" role="img" aria-label="Dark stormy backdrop with a parked car"></section>
<div class="abs logo">Kavrelon Cell</div>
<div class="abs tagline">CALL AND RELEX WITH SERVICES</div>
<nav class="abs nav">
  <a class="active">Home</a><a>About</a><a>Features</a><a>Blog</a><a>Order Now</a><a>Contacts</a>
</nav>
<div class="abs heading call-label">Call us now</div>
<div class="abs call-phone">+1 555 0142 7788</div>
<div class="abs call-url">www.kavreloncell-power.com</div>
<div class="abs hero-products" role="img" aria-label="Group of red batteries in various sizes"></div>

<!-- intro -->
<section class="intro"></section>
<div class="abs heading eyebrow-white">Best in city</div>
<h1 class="abs heading intro-title">Trusted batteries servies<br>in New York</h1>
<p class="abs intro-text">Quisque sollicitudin feugiat risus, eu posuere ex euismod eu. Phasellus hendrerit, massa efficitur dapibus pulvinar, sapien eros sodales ante, euismod aliquet nulla metus a mauris.Quisque sollicitudin feugiat risus, eu posuere ex euismod eu. Phasellus hendrerit, massa efficitur dapibus pulvinar, sapien eros sodales ante, euismod aliquet nulla metus a mauris.</p>
<div class="btn btn-white">Read more</div>

<form class="abs booking">
  <div class="heading booking-head">Book a <span>batteries</span></div>
  <div class="field" style="left:26px;top:82px;width:128px">First name</div>
  <div class="field" style="left:170px;top:82px;width:128px">Last name</div>
  <div class="field" style="left:26px;top:138px;width:128px">Phone</div>
  <div class="field" style="left:170px;top:138px;width:128px">Email</div>
  <div class="field" style="left:26px;top:194px;width:272px">Choose battery</div>
  <div class="field" style="left:26px;top:250px;width:272px">Description</div>
  <div class="btn btn-submit">Submit</div>
</form>

<!-- products -->
<div class="abs heading section-eyebrow" style="top:1127px">Our</div>
<h2 class="abs heading section-title" style="top:1155px">Kavrelon batteries</h2>

<article class="card" style="left:160px">
  <div class="card-photo" role="img" aria-label="Small red rechargeable battery"></div>
  <h3 class="heading">Rechargeable</h3>
  <p>Quisque sollicitudin feugiat risus, eu posuere ex euismod eu. in Phasellus hendrerit.</p>
  <div class="heading price">$150</div>
  <div class="btn">Read more</div>
</article>
<article class="card featured" style="left:470px">
  <div class="card-photo" role="img" aria-label="Small red non-rechargeable battery"></div>
  <h3 class="heading">Non-rechargeable</h3>
  <p>Quisque sollicitudin feugiat risus, eu posuere ex euismod eu. in Phasellus hendrerit.</p>
  <div class="heading price">$250</div>
  <div class="btn">Read more</div>
  <svg class="corner" width="56" height="56" viewBox="0 0 56 56"><polygon points="56,0 56,56 0,56" fill="#141414"/><polygon points="38,28 41,36 49,36 43,41 45,49 38,44 31,49 33,41 27,36 35,36" fill="#f6c21c"/></svg>
</article>
<article class="card" style="left:776px">
  <div class="card-photo" role="img" aria-label="Small red wet-cell battery"></div>
  <h3 class="heading">Wet-cell</h3>
  <p>Quisque sollicitudin feugiat risus, eu posuere ex euismod eu. in Phasellus hendrerit.</p>
  <div class="heading price">$200</div>
  <div class="btn">Read more</div>
</article>

<!-- services -->
<section class="services" role="img" aria-label="Sports car on a wet night road"></section>
<div class="abs heading section-eyebrow" style="top:1712px">We do best</div>
<h2 class="abs heading section-title" style="top:1744px;color:var(--white)">Than you wish</h2>

<div class="feature-icon" style="left:174px;top:1848px"><svg width="22" height="22" viewBox="0 0 24 24"><polygon points="12,2 15,9 22,9 16.5,13.5 18.5,21 12,16.5 5.5,21 7.5,13.5 2,9 9,9" fill="#fff"/></svg></div>
<div class="heading feature-title" style="left:259px;top:1838px">Home pickup</div>
<p class="feature-text" style="left:262px;top:1876px">Quisque sollicitudin feugiat risus, eu posuere ex euismod eu. Phasellus hendrerit, massa efficitur.</p>

<div class="feature-icon" style="left:680px;top:1848px"><svg width="20" height="22" viewBox="0 0 20 22"><path d="M3 1h14M3 21h14M5 1c0 6 10 6 10 10S5 15 5 21M15 1c0 6-10 6-10 10s10 4 10 10" stroke="#fff" stroke-width="2" fill="none"/></svg></div>
<div class="heading feature-title" style="left:767px;top:1838px">Fast booking</div>
<p class="feature-text" style="left:770px;top:1876px">Quisque sollicitudin feugiat risus, eu posuere ex euismod eu. Phasellus hendrerit, massa efficitur.</p>

<div class="feature-icon" style="left:174px;top:1986px"><svg width="22" height="22" viewBox="0 0 22 22"><path d="M3 20V8h3v3h3V6h4v5h3V8h3v12z" fill="#fff"/></svg></div>
<div class="heading feature-title" style="left:259px;top:1976px">Bonuses</div>
<p class="feature-text" style="left:262px;top:2016px">Quisque sollicitudin feugiat risus, eu posuere ex euismod eu. Phasellus hendrerit, massa efficitur.</p>

<div class="feature-icon" style="left:680px;top:1986px"><svg width="22" height="22" viewBox="0 0 22 22"><circle cx="11" cy="11" r="6" fill="none" stroke="#fff" stroke-width="4" stroke-dasharray="3 2"/><circle cx="11" cy="11" r="2.5" fill="#fff"/></svg></div>
<div class="heading feature-title" style="left:767px;top:1976px">Searching</div>
<p class="feature-text" style="left:770px;top:2016px">Quisque sollicitudin feugiat risus, eu posuere ex euismod eu. Phasellus hendrerit, massa efficitur.</p>

<div class="btn btn-red" style="left:539px;top:2127px;width:124px;height:36px">Read more</div>

<!-- about -->
<div class="abs heading about-eyebrow">About</div>
<h2 class="abs heading about-title">Kavrelon Cell</h2>
<p class="abs about-text">Quisque sollicitudin feugiat risus, eu posuere ex euismod eu. Phasellus hendrerit, massa efficitur dapibus pulvinar, sapien eros sodales ante, euismod aliquet nulla metus a mauris.Quisque sollicitudin feugiat risus, Quisque sollicitudin feugiat risus, eu posuere ex euismod eu. Phasellus hendrerit,</p>
<div class="btn btn-dark">Read more</div>

<div class="about-icon" style="left:165px"><svg width="26" height="22" viewBox="0 0 26 22"><path d="M2 14l5-5 5 4 5-6 7 7M2 19h22" stroke="#141414" stroke-width="2" fill="none"/></svg></div>
<div class="about-icon" style="left:223px"><svg width="26" height="26" viewBox="0 0 26 26"><circle cx="13" cy="13" r="4" fill="none" stroke="#141414" stroke-width="2"/><circle cx="13" cy="13" r="8.5" fill="none" stroke="#141414" stroke-width="2"/></svg></div>
<div class="about-icon" style="left:281px"><svg width="22" height="26" viewBox="0 0 22 26"><rect x="7" y="2" width="8" height="13" rx="4" fill="#141414"/><path d="M3 12c0 5 4 8 8 8s8-3 8-8M11 20v4" stroke="#141414" stroke-width="2" fill="none"/></svg></div>
<div class="about-icon hot" style="left:339px"><svg width="16" height="26" viewBox="0 0 16 26"><rect x="2" y="4" width="12" height="20" rx="2" fill="none" stroke="#ee3232" stroke-width="2"/><rect x="5" y="1" width="6" height="3" fill="#ee3232"/><rect x="5" y="8" width="6" height="13" fill="#ee3232"/></svg></div>
<div class="about-icon" style="left:397px"><svg width="24" height="24" viewBox="0 0 24 24"><path d="M3 21l6-6M9 15l10-10 2 2-10 10z" stroke="#141414" stroke-width="2" fill="none"/></svg></div>

<div class="abs about-products" role="img" aria-label="Assorted red automotive batteries"></div>

<!-- testimonials -->
<section class="testimonials" role="img" aria-label="Grid of happy client portraits in monochrome"></section>
<div class="abs heading section-eyebrow" style="top:2786px">Happy client's</div>
<h2 class="abs heading section-title" style="top:2822px;color:var(--white)">Testimonials</h2>

<article class="quote" style="left:160px">
  <p>Quisque sollicitudin feugiat risus, eu posuere ex euismod eu. Phasellus hendrerit, massa efficitur.Quisque sollicitudin feugiat risus.</p>
  <div class="avatar" role="img" aria-label="Client portrait"></div>
  <div class="heading name">Maren Holt</div>
  <div class="role">Business man</div>
</article>
<article class="quote" style="left:622px">
  <p>Quisque sollicitudin feugiat risus, eu posuere ex euismod eu. Phasellus hendrerit, massa efficitur.Quisque sollicitudin feugiat risus.</p>
  <div class="avatar" role="img" aria-label="Client portrait"></div>
  <div class="heading name">Maren Holt</div>
  <div class="role">Business man</div>
</article>

<!-- cta -->
<section class="cta"></section>
<div class="abs heading cta-text">We are ready to take your call 24 hours, 7 days!</div>
<div class="abs heading cta-phone">+1 555 0142 7788</div>

<!-- footer -->
<footer class="footer"></footer>
<div class="heading foot-head" style="left:160px;top:3443px">About Kavrelon Cell</div>
<div class="heading foot-head" style="left:483px;top:3436px">Services</div>
<div class="heading foot-head" style="left:804px;top:3436px">Contact</div>
<div class="foot-rule" style="left:160px"></div>
<div class="foot-rule" style="left:483px"></div>
<div class="foot-rule" style="left:804px"></div>

<p class="foot-text" style="left:165px;top:3517px;width:260px">Quisque sollicitudin feugiat risus, eu posuere ex euismod eu. Phasellus hendrerit, massa efficitur.Quisque sollicitudin feugiat risus, eu posuex euismod eu.</p>
<div class="social"><span></span><span></span><span class="hot"></span><span></span></div>

<ul class="foot-list" style="left:483px;top:3519px">
  <li>Non-Rechargeable Batteries</li>
  <li>Rechargeable Batteries</li>
  <li>Wet-Cell Batteries</li>
  <li>Metal Oxide Batteries</li>
</ul>

<div class="contact-row" style="top:3523px"><svg width="12" height="16" viewBox="0 0 12 16"><path d="M6 0a6 6 0 0 0-6 6c0 4 6 10 6 10s6-6 6-10a6 6 0 0 0-6-6zm0 8.5A2.5 2.5 0 1 1 6 3.5a2.5 2.5 0 0 1 0 5z" fill="#fff"/></svg><span>48 Larkfield Avenue, Brookmere,<br>NY 10482</span></div>
<div class="contact-row" style="top:3571px"><svg width="12" height="16" viewBox="0 0 12 16"><rect x="2" y="1" width="8" height="14" rx="1.5" fill="none" stroke="#fff" stroke-width="2"/></svg><span>+1 555 0142 7788</span></div>
<div class="contact-row" style="top:3605px"><svg width="12" height="16" viewBox="0 0 12 16"><rect x="0" y="4" width="12" height="9" fill="#fff"/><path d="M0 4l6 5 6-5" stroke="#141414" stroke-width="1.3" fill="none"/></svg><span>hello@kavreloncell-power.com</span></div>
<div class="contact-row" style="top:3638px"><svg width="12" height="16" viewBox="0 0 12 16"><path d="M1 1l10 7-4.5 1 2.5 5-2 1-2.5-5L1 12z" fill="#fff"/></svg><span>www.kavreloncell-power.com</span></div>

<div class="abs copyright">Copyright © 2021 www.kavreloncell-power.com</div>

</body>
</html>
```